Harbinger Slabworks, Inc. Business Card

Create a business card that is eye catching and based around concrete sawcutting. I've attached our current business card and logo for reference. We like aspects of the current business card, but it is starting to feel very loud and lost. We would like something that is still fun but is more modern and streamlined.

```html
<!DOCTYPE html>
<html lang="en">
<head>
<meta charset="utf-8">
<title>Harbinger Slabworks, Inc. Business Card</title>
<link href="https://fonts.googleapis.com/css2?family=Open+Sans:wght@400;600;700&display=swap" rel="stylesheet">
<style>
  :root {
    --stage: #222224;
    --card-dark: #1f1f23;
    --navy: #1c2660;
    --red: #d0202a;
    --yellow: #f5cc12;
    --white: #ffffff;
    --grey: #c9c9cf;
  }
  * { box-sizing: border-box; margin: 0; padding: 0; }
  html, body { width: 1200px; height: 780px; overflow: hidden; }
  body {
    background: var(--stage);
    font-family: "Open Sans", Arial, sans-serif;
    position: relative;
  }
  .card {
    position: absolute;
    width: 520px;
    height: 297px;
    background: var(--card-dark);
    overflow: hidden;
    box-shadow: 0 14px 30px rgba(0,0,0,.45);
  }
  .card--front { left: 50px; top: 242px; }
  .card--back { left: 630px; top: 242px; }

  .front-panel { position: absolute; inset: 0; }

  .brand-front {
    position: absolute;
    left: 28px; top: 108px;
    width: 170px;
    display: flex; align-items: center; gap: 10px;
  }
  .brand-mark {
    flex: none;
    width: 22px; height: 22px;
    border-radius: 50%;
    background: var(--red);
  }
  .brand-name {
    color: var(--white);
    font-weight: 700;
    font-size: 17px;
    line-height: 1.2;
    letter-spacing: .5px;
  }

  .details {
    position: absolute;
    right: 22px; top: 26px;
    text-align: right;
  }
  .person {
    font-weight: 700;
    font-size: 22px;
    letter-spacing: .5px;
    text-transform: uppercase;
    line-height: 1;
  }
  .person__first { color: var(--red); }
  .person__last { color: var(--yellow); }
  .name-tab {
    position: absolute;
    right: 0; top: 26px;
    width: 10px; height: 22px;
    background: var(--red);
  }
  .address {
    color: var(--white);
    font-size: 10.5px;
    line-height: 1.45;
    margin-top: 8px;
  }
  .contacts { list-style: none; margin-top: 4px; }
  .contacts li {
    color: var(--white);
    font-size: 10.5px;
    line-height: 1.55;
    display: flex; justify-content: flex-end; align-items: center; gap: 6px;
  }
  .contacts svg { width: 10px; height: 10px; flex: none; }

  .services {
    position: absolute;
    right: 22px; bottom: 20px;
    text-align: right;
  }
  .services__title {
    color: var(--red);
    font-weight: 700;
    font-size: 12px;
    text-transform: uppercase;
    margin-bottom: 2px;
  }
  .services ul { list-style: none; }
  .services li {
    color: var(--white);
    font-size: 10.5px;
    text-transform: uppercase;
    line-height: 1.5;
    display: flex; justify-content: flex-end; align-items: center; gap: 8px;
  }
  .dot { width: 6px; height: 6px; border-radius: 50%; }
  .dot--red { background: var(--red); }
  .dot--yellow { background: var(--yellow); }

  .back-pattern {
    position: absolute; inset: 0;
    background: radial-gradient(circle at 50% 50%, #2b2b30 0%, #222226 55%, #1b1b1f 100%);
  }
  .brand-back {
    position: absolute;
    left: 50%; top: 50%;
    transform: translate(-50%, -50%);
    display: flex; flex-direction: column; align-items: center; gap: 12px;
  }
  .brand-back .brand-mark { width: 30px; height: 30px; }
  .brand-back .brand-name { font-size: 20px; text-align: center; }
</style>
</head>
<body>

  <section class="card card--front" aria-label="Business card front">
    <svg class="front-panel" viewBox="0 0 520 297" preserveAspectRatio="none" aria-hidden="true">
      <path d="M0 0 H200 C250 70 250 220 140 297 H0 Z" fill="var(--navy)"/>
      <path d="M200 0 C250 70 250 220 140 297" fill="none" stroke="var(--red)" stroke-width="7"/>
    </svg>

    <div class="brand-front">
      <span class="brand-mark"></span>
      <span class="brand-name">Harbinger Slabworks, Inc.</span>
    </div>

    <span class="name-tab"></span>
    <div class="details">
      <p class="person"><span class="person__first">Dana</span> <span class="person__last">Marlowe</span></p>
      <p class="address">48 Quarry Lane,<br>Millbrook, NJ 07999</p>
      <ul class="contacts">
        <li>855.555.0142 (Office)
          <svg viewBox="0 0 10 10"><path d="M2 1 L4 1 L4.6 3 L3.4 3.8 C4 5.2 5 6.2 6.2 6.8 L7 5.5 L9 6 L9 8 C9 8.6 8.5 9 8 9 C4.5 8.8 1.2 5.5 1 2 C1 1.5 1.4 1 2 1 Z" fill="var(--red)"/></svg>
        </li>
        <li>973.555.0187 (Cell)
          <svg viewBox="0 0 10 10"><rect x="2.5" y="0.8" width="5" height="8.4" rx="1" fill="none" stroke="var(--yellow)" stroke-width="1.1"/></svg>
        </li>
        <li>www.HarbingerSlabworks.com
          <svg viewBox="0 0 10 10"><circle cx="5" cy="5" r="4" fill="none" stroke="var(--red)" stroke-width="1.1"/><path d="M1 5 H9 M5 1 C3 3.5 3 6.5 5 9 M5 1 C7 3.5 7 6.5 5 9" fill="none" stroke="var(--red)" stroke-width=".8"/></svg>
        </li>
        <li>Dana@HarbingerSlabworks.com
          <svg viewBox="0 0 10 10"><rect x="1" y="2" width="8" height="6" fill="none" stroke="var(--yellow)" stroke-width="1.1"/><path d="M1 2 L5 5.5 L9 2" fill="none" stroke="var(--yellow)" stroke-width="1"/></svg>
        </li>
      </ul>
    </div>

    <div class="services">
      <p class="services__title">Our Services</p>
      <ul>
        <li>Wall Sawing <span class="dot dot--red"></span></li>
        <li>Core Drilling <span class="dot dot--yellow"></span></li>
        <li>Slab Sawing <span class="dot dot--red"></span></li>
        <li>Breaking &amp; Removal <span class="dot dot--yellow"></span></li>
      </ul>
    </div>
  </section>

  <section class="card card--back" aria-label="Business card back">
    <div class="back-pattern" role="img" aria-label="Faint repeating emblem pattern across the dark card back"></div>
    <div class="brand-back">
      <span class="brand-mark"></span>
      <span class="brand-name">Harbinger Slabworks, Inc.</span>
    </div>
  </section>

</body>
</html>
```